Spa Resort Website

UPDATE:
Note that for the home page we are intending to have a slideshow showcasing elements of the resort, as per:
* www.brellowpools.co.nz
* www.vantrilo.com
* www.gladwick-journeys.com
We also need to know how you intend to use the colours to denote subsections, as per the brief below.
Also...the sliders denoting Elegant vs Bold etc seem to have lost their settings. I have reset them to how I believe we set them a couple of weeks ago, but there may be minor differences.
=============================================
We are developing a website for Taupo Wenlocks, a resort in Taupo, New Zealand.
While we have been provided with a site layout and basic colour scheme, the implementation of this design does not meet the client's needs for a modern, inviting looking site.
We require a designer to work within the outline structure of the site and provide design elements to lift the design. We envisage that these design elements would include styling of the menus, building of the colour schemes from the base colours, home page design.
If you are unsure of the parameters please post a question indicating elements you would like to change and we can comment on feasibility.
We have attached the original design concept and some of the wire framing that we developed from that.
The site has four major sections, each requiring its own, subtly different, colour scheme - these schemes are to be based on the colours in the client's logo (attached). Obviously there does need to be consistency in the colour schemes across the site. The colours from the logo apply as follows:
* Stay (accommodation) - "Orange"
* Soak (Hot Springs and water park) - "Green"
* Soothe (Spa Resort) - "Beige"
* Savour (Summary of experience) - "Choc Brown"
We require the design for 2 pages:
* Home
* Detail Page (eg Family Accommodation)
Design must be flexible in that if we decide at a later date to add another block to the RH area (for example) we are able to while maintaining the integrity of the design.
Menu items include dropdowns.
We are not happy with the current layout of the HOME page and require a full redesign of this.
The resort is 5 star, but also offers camping facilities. The design therefore needs to reflect the high quality of the resort, while also being accessible to those on a budget.
The following sites can be considered reference sites for the look and feel we are seeking:
* www.brellowpools.co.nz
* www.vantrilo.com
Final deliverable is preferred in layered PNG, but .eps is acceptable. .ai is not acceptable.

```html
<!DOCTYPE html>
<html lang="en">
<head>
<meta charset="utf-8">
<title>Taupo Wenlocks Spa Resort</title>
<link rel="stylesheet" href="https://fonts.googleapis.com/css2?family=Archivo+Black&family=Arimo:ital,wght@0,400;0,700;1,400;1,700&display=swap">
<style>
:root{
  --page:#d5e7fb;
  --peach:#fdd4a3;
  --sage:#94c4a8;
  --cream:#fff1d8;
  --tan:#d9b86f;
  --band:#2a394c;
  --band-edge:#1b2633;
  --bubble:#eef5fc;
  --orange:#ff6411;
  --orange-dark:#d44e05;
  --blue:#4d9ce9;
  --blue-light:#74b3f1;
  --panel:#dbeafb;
  --tab:#4c93e0;
  --tab-dark:#2a3a4e;
  --brown:#5b4515;
  --olive:#8a7a4a;
  --footer:#1c3e6c;
  --footer-deep:#15335c;
  --footer-link:#8fb3dc;
  --footer-head:#a7c6ea;
  --gold:#e7cf95;
  --base:#2d3e55;
  --green:#2f9c5c;
  --text:#222;
}
*{box-sizing:border-box;margin:0;padding:0}
html,body{width:1200px;height:900px;overflow:hidden}
body{background:var(--page);font-family:Arimo,Arial,sans-serif;color:var(--text);position:relative}
.abs{position:absolute}

/* teaser strip */
.teaser{top:0;height:57px;width:240px;font-size:12.5px;padding:9px 12px;border:1px solid rgba(0,0,0,.12)}
.teaser p{white-space:nowrap;overflow:hidden}
.teaser .more{position:absolute;right:16px;bottom:9px;font-size:12px;color:#8a7d6a}
.t1{left:120px;background:var(--peach)}
.t2{left:360px;background:var(--sage)}
.t3{left:600px;background:var(--cream)}
.t4{left:840px;background:var(--tan)}

/* testimonial band */
.band{left:107px;top:57px;width:986px;height:120px;background:var(--band)}
.say{left:130px;top:104px;width:100px;font:italic 700 15px/15px Arimo,Arial,sans-serif;color:var(--olive);text-align:center;letter-spacing:.3px}
.say-more{left:190px;top:138px;font-size:12px;color:#bba16a}
.bubble{left:251px;top:81px;width:590px;height:72px;background:var(--bubble);border-radius:8px;padding:9px 12px;font:italic 13px/24px Arimo,Arial,sans-serif;color:#5a5a3a}
.bubble::before{content:"";position:absolute;left:-10px;top:28px;border:8px solid transparent;border-right:10px solid var(--bubble);border-left:0}
.bubble cite{position:absolute;right:30px;bottom:8px;font-style:italic}
.book-big{left:850px;top:83px;width:220px;height:68px;background:linear-gradient(#ff7a2a,var(--orange));border:2px solid #ffb07a;border-radius:7px;color:#fff;font:26px/64px "Archivo Black",Arial,sans-serif;text-align:center;text-shadow:0 1px 1px rgba(0,0,0,.35)}

/* main */
.fold{top:177px;width:13px;height:10px}
.main{left:120px;top:177px;width:960px;height:421px;background:linear-gradient(90deg,#3d8ee6,var(--blue) 60%,var(--blue-light))}
.h-best{left:140px;top:192px;font:25px/30px "Archivo Black",Arial,sans-serif;color:#fff;text-shadow:0 1px 2px rgba(0,0,0,.3)}
.see-all{left:570px;top:204px;font-size:15px;color:#d8eafc}
.pkg-panel{left:130px;top:237px;width:588px;height:287px;background:var(--panel)}
.tab{left:131px;width:158px;height:70px;background:linear-gradient(#5aa2ec,var(--tab));border:1px solid #7cb5ee;color:#fff;font:700 15px/70px Arimo,Arial,sans-serif;padding-left:9px;text-shadow:0 1px 1px rgba(0,0,0,.3)}
.tab.active{background:none;border:none}
.pkg-title{left:371px;top:260px;font:20px/26px "Archivo Black",Arial,sans-serif;color:var(--brown)}
.photo-frame{left:350px;top:296px;width:200px;height:157px;background:#a9c8e8;border:1px solid #7fa8d2}
.photo{left:370px;top:313px;width:160px;height:123px;background:linear-gradient(180deg,#9cd34a,#6fae34 45%,#c9a98a 70%,#e7e2d5)}
.pkg-desc{left:560px;top:290px;width:150px;font-size:12.5px;line-height:24px;color:#333}
.pkg-meta{left:560px;top:388px;font-size:10px;line-height:24px;color:#3b2f10}
.start{left:370px;top:470px;font-size:10px;color:#3b2f10}
.price{left:370px;top:481px;font-size:20px;color:#e0560f}
.price-note{left:370px;top:504px;font-size:10px;color:#e8a66d}
.book-small{left:550px;top:477px;width:100px;height:36px;background:var(--orange);border:2px solid #ff9a55;color:#fff;font:700 13px/32px Arimo,Arial,sans-serif;text-align:center}
.or{left:654px;top:489px;font-size:11px;color:#d9a35a}
.more-detail{left:669px;top:485px;font:700 13px/13px Arimo,Arial,sans-serif;color:#4b3a10;text-align:right}

.subscribe{left:130px;top:537px;width:349px;height:47px;background:linear-gradient(#fff,#e4eef9);border:1px solid #3b7bc4}
.subscribe span{position:absolute;left:13px;top:18px;font-size:12.5px;color:#6c8fb8}
.sub-btn{left:239px;top:11px;width:100px;height:25px;background:linear-gradient(#45b575,var(--green));border:1px solid #1f7c47;color:#fff;font:700 12.5px/23px Arimo,Arial,sans-serif;text-align:center}
.social{left:490px;top:537px;width:229px;height:47px;background:#8cc0f4}
.social i{position:absolute;top:6px;width:32px;height:32px;border-radius:50%;border:2px solid #fff;box-shadow:0 1px 2px rgba(0,0,0,.3)}

/* aside */
.aside{left:730px;top:177px;width:340px;height:409px;background:linear-gradient(#c5e0fa,#fff 95px)}
.brand{left:742px;top:187px;display:flex;flex-direction:column;align-items:center;gap:6px;width:104px}
.brand i{width:34px;height:34px;border-radius:50%;border:4px solid #e3782d}
.brand b{font:700 13px/14px Arimo,Arial,sans-serif;color:#111;white-space:nowrap}
.rule{left:741px;width:320px;height:1px;background:#5b4a2b}
.aside-lead{left:742px;top:281px;width:318px;font:700 12.5px/24px Arimo,Arial,sans-serif;color:#000;letter-spacing:.3px}
.aside-body{left:742px;top:366px;width:318px;font-size:12.5px;line-height:24px;color:#222}
.aside-body p+p{margin-top:24px}
.aside-more{left:1019px;top:561px;font-size:12.5px;color:#7aaee4}

/* footer */
.footer{left:120px;top:598px;width:960px;height:254px;background:linear-gradient(var(--footer-deep),var(--footer))}
.col{top:630px}
.col h3{font:700 15px/20px Arimo,Arial,sans-serif;color:var(--footer-head);margin-bottom:6px;letter-spacing:.3px}
.col h4{font:700 12.5px/24px Arimo,Arial,sans-serif;color:var(--footer-head);padding-left:2px;letter-spacing:.3px}
.col li{list-style:none;font-size:12.5px;line-height:24px;color:var(--footer-link);padding-left:2px}
.c1{left:190px}.c2{left:369px}.c3{left:608px}
.f-brand{left:870px;top:624px;width:120px;display:flex;flex-direction:column;align-items:center;gap:6px}
.f-brand i{width:34px;height:34px;border-radius:50%;border:4px solid #e3782d;box-shadow:0 0 18px #3d7fc8}
.f-brand b{font:700 13px/14px Arimo,Arial,sans-serif;color:#0c1a2c;white-space:nowrap}
.address{left:830px;top:697px;width:200px;text-align:center;font-size:12.5px;line-height:12px;color:var(--gold)}
.address h5{font:700 13px/16px Arimo,Arial,sans-serif;margin-bottom:8px}
.address p+p{margin-top:12px}
.base{left:120px;top:852px;width:960px;height:48px;background:linear-gradient(#3a4c63,var(--base));border:1px solid #4f6680;color:#b9c6d6;font-size:10px;line-height:46px;text-align:center}
</style>
</head>
<body>

<div class="abs teaser t1"><p>placerat, pellentesque! Arcu urna etiam</p><span class="more">More &gt;</span></div>
<div class="abs teaser t2"><p>urna lectus arcu est, porta, diam placerat</p><span class="more">More &gt;</span></div>
<div class="abs teaser t3"><p>cus egestas? Sit! Purus, scelerisque sit,</p><span class="more">More &gt;</span></div>
<div class="abs teaser t4"><p>dignissim. Dignissim, pulvinar nunc,</p><span class="more">More &gt;</span></div>

<section class="abs band"></section>
<div class="abs say">I would like<br>to say</div>
<span class="abs say-more">More &gt;</span>
<blockquote class="abs bubble">“Amet platea cursus ac? Scelerisque sociis. Turpis ut scelerisque, amet? Odio, dolor duis lacus purus nunc turpis, dapibus. Ut vut, lorem amet aliquam. Lundium. Mid.”<cite>- Mara Ellison</cite></blockquote>
<a class="abs book-big">Book Now</a>

<svg class="abs fold" style="left:107px" viewBox="0 0 13 10"><polygon points="0,0 13,0 13,10" fill="var(--band-edge)"/></svg>
<svg class="abs fold" style="left:1080px" viewBox="0 0 13 10"><polygon points="0,0 13,0 0,10" fill="var(--band-edge)"/></svg>

<main class="abs main"></main>
<h2 class="abs h-best">Our Best Package</h2>
<a class="abs see-all">See all our package &gt;</a>
<div class="abs pkg-panel"></div>

<svg class="abs" style="left:131px;top:238px" width="180" height="71" viewBox="0 0 180 71">
  <defs><linearGradient id="tabDark" x1="0" y1="0" x2="0" y2="1"><stop offset="0" stop-color="#3c4f66"/><stop offset="1" stop-color="var(--tab-dark)"/></linearGradient></defs>
  <polygon points="0,0 158,0 178,35 158,70 0,70" fill="url(#tabDark)" stroke="#6c87a6"/>
</svg>
<div class="abs tab active" style="top:238px">Package 1</div>
<div class="abs tab" style="top:310px">Package 2</div>
<div class="abs tab" style="top:382px">Package 3</div>
<div class="abs tab" style="top:454px">Package 4</div>

<h3 class="abs pkg-title">The Family Spa</h3>
<div class="abs photo-frame"></div>
<div class="abs photo" role="img" aria-label="Hot stone massage treatment on a spa bed with bamboo backdrop"></div>
<p class="abs pkg-desc">Placerat cursus. Ac etiam habitasse tortor, in tincid-unt, amet, vel.</p>
<p class="abs pkg-meta">Accomodation : 1 Luxury lodges<br>Breakfast for 5 person</p>
<span class="abs start">Start From</span>
<span class="abs price">$529</span>
<span class="abs price-note">for 5 person, add $39 for more</span>
<a class="abs book-small">Book Now</a>
<span class="abs or">or</span>
<a class="abs more-detail">More<br>Detail</a>

<form class="abs subscribe"><span>Subscribe to get Latest Promo</span><div class="abs sub-btn">Subscribe</div></form>
<nav class="abs social" aria-label="Social links">
  <i style="left:23px;background:#3b5b98"></i>
  <i style="left:61px;background:#35b6e6"></i>
  <i style="left:99px;background:#2c5a85"></i>
  <i style="left:137px;background:#e8e8ee"></i>
  <i style="left:175px;background:#f58a1f"></i>
</nav>

<aside class="abs aside"></aside>
<div class="abs brand"><i></i><b>Taupo Wenlocks</b></div>
<div class="abs rule" style="top:273px"></div>
<p class="abs aside-lead">Stay in Quality Accommodation, Soak in His-toric Hot Springs, Soothe in the Spa &amp; Savour the Experience of Taupo Wenlocks.</p>
<div class="abs rule" style="top:356px"></div>
<div class="abs aside-body">
  <p>Adipiscing tortor proin odio, ultrices penatibus rhoncus in tincidunt hac, aliquet dapibus, urna cursus non turpis nec eros, mattis ut magna mid elementum diam.</p>
  <p>eu mid odio mid ac placerat, est augue facilisis, odio, dictumst montes? Aliquet odio natoque turpis, a magna est magna? Augue! Dictumst platea, turpis, parturient facilisis.</p>
</div>
<a class="abs aside-more">More &gt;</a>

<footer class="abs footer"></footer>
<div class="abs col c1"><h3>Spa resort</h3><h4>Accomodation</h4><ul><li>Spa Chalets</li><li>Luxury Lodges</li><li>Motels</li><li>Cabins</li><li>Campsites</li><li>Motorthomes /RVs</li></ul></div>
<div class="abs col c2"><h3>Hot Spring</h3><h4>Thermal Mineral Bathing</h4><ul><li>Outdoor Pools</li><li>Water Playground</li><li>Dragon Hydroslide</li></ul></div>
<div class="abs col c3"><h3>Living Water Spa</h3><h4>Spa Treatment</h4><ul><li>Massages</li><li>Body Treatments</li><li>Face Treatments</li><li>Pedicure</li><li>Manicure</li></ul></div>
<div class="abs f-brand"><i></i><b>Taupo Wenlocks</b></div>
<address class="abs address" style="font-style:normal">
  <h5>Address :</h5>
  <p>Kererū Ridge Highway<br>Lake Harrowmere<br>New Zealand</p>
  <p>Ph : +64 7000 1428<br>Fx : +64 7000 1429</p>
</address>
<div class="abs base">Copyright © Taupo Wenlocks 2011, All rights reserved</div>

</body>
</html>
```